Marketing Skill "Workouts"; Design for an e-mail attachment highlighting Marketing training subjects

I am a freelance marketing trainer based in Singapore and need to e-mail out an attachment (probably saved as a PDF) to potential clients showing the training services I offer. These clients are all large blue-chip multinational companies so the attachment needs to look professional/high quality when opened on a computer.

My Company is called "Clearpath Marketing" (logo attached)

I am assuming the size should be A4 one sided colour.

I have attached some files that show best-attempts so far. These contain the key information, but the layouts all still look rather pedestrian. I am looking for something that looks a bit more dynamic but remains clear/easy to read.

Target Market(s)

HR/Marketing managers in multinational firms, mainly consumer goods

Industry/Entity Type

Marketing

Font styles to use
Sans Serif

Colors

Designer to choose colors to be used in the design.

Requirements
Must have
• Must look modern, up-to-date, professional.
Should not have
• Not gimmicky, like a cheap deal

```html
<!DOCTYPE html>
<html lang="en">
<head>
<meta charset="utf-8">
<title>Marketing Skill Workouts – Clearpath Marketing</title>
<link rel="stylesheet" href="https://fonts.googleapis.com/css2?family=Montserrat:wght@600;700;800&family=Open+Sans:ital,wght@0,400;0,600;0,700;1,700&display=swap">
<style>
:root{
  --red:#c8202a;
  --red-dark:#9e1720;
  --charcoal:#2b2b2d;
  --ink:#333336;
  --grey-text:#5a5a5e;
  --rule:#d7d7d9;
  --white:#ffffff;
}
*{box-sizing:border-box;margin:0;padding:0}
html,body{width:849px;height:1200px;overflow:hidden;background:var(--white)}
.sheet{position:relative;width:849px;height:1200px;overflow:hidden;font-family:"Open Sans",Arial,sans-serif;color:var(--ink)}

.hero-photo{position:absolute;left:0;top:0;width:849px;height:470px;
  background:linear-gradient(180deg,#fafafa 0%,#e8e8e8 22%,#b9b9b9 55%,#6d6d6f 80%,#3b3b3d 100%)}
.hero-shade{position:absolute;left:0;top:250px;width:849px;height:150px;
  background:linear-gradient(180deg,rgba(40,40,42,0) 0%,rgba(40,40,42,.55) 100%)}

.contact{position:absolute;left:34px;top:20px;display:flex;flex-direction:column;gap:12px;font-size:17px;color:var(--grey-text)}
.contact-row{display:flex;align-items:center;gap:12px}
.contact-icon{width:28px;height:28px;border-radius:50%;background:var(--red);display:flex;align-items:center;justify-content:center}

.brand{position:absolute;right:34px;top:26px;display:flex;align-items:center;gap:14px}
.brand-mark{width:64px;height:64px;border-radius:50%;background:var(--red)}
.brand-text{display:flex;flex-direction:column}
.brand-name{font-family:"Montserrat",Arial,sans-serif;font-weight:800;font-size:30px;color:var(--charcoal);line-height:1.05}
.brand-tag{font-size:13px;font-weight:600;color:var(--grey-text);margin-top:4px}

.title{position:absolute;left:34px;top:300px;color:var(--white);font-family:"Montserrat",Arial,sans-serif}
.title-line{font-size:38px;font-weight:800;letter-spacing:.5px;line-height:1}
.title-accent{font-size:40px;font-weight:800;font-style:italic;color:var(--red);line-height:1.1;margin-top:4px}

.promo-band{position:absolute;left:0;top:398px;width:849px;height:72px;background:var(--charcoal)}
.promo-question{position:absolute;left:34px;top:20px;font-family:"Montserrat",Arial,sans-serif;font-weight:800;font-size:28px;color:var(--white)}
.promo-answer{position:absolute;left:402px;top:-8px;width:447px;height:80px;background:var(--red);padding:12px 20px;color:var(--white);font-size:16px;font-weight:600;line-height:1.4}

.section-title{font-family:"Montserrat",Arial,sans-serif;font-weight:800;font-size:31px;color:var(--charcoal);margin-bottom:16px}
.topics{position:absolute;left:34px;top:500px;width:340px}
.topic-list{list-style:none}
.topic-list li{font-size:15.5px;line-height:1.45;padding:9px 0 9px 12px;border-bottom:1px solid var(--rule);position:relative}
.topic-list li::before{content:"•";position:absolute;left:0}

.divider{position:absolute;left:401px;top:505px;width:2px;height:440px;background:var(--rule)}

.benefits{position:absolute;left:425px;top:500px;width:390px}
.benefit-list{list-style:none}
.benefit{display:flex;align-items:center;gap:20px;min-height:82px}
.benefit-icon{flex:0 0 52px;height:52px}
.benefit-text{font-size:17.5px;line-height:1.4;color:var(--ink)}

.why-band{position:absolute;left:0;top:975px;width:849px;height:225px;background:var(--charcoal);padding:22px 34px;color:#d9d9db}
.why-head{font-family:"Montserrat",Arial,sans-serif;font-weight:700;font-size:25px;color:var(--white)}
.why-head em{color:var(--red);font-style:normal;font-weight:800}
.why-body{margin-top:14px;font-size:17px;line-height:1.55}
</style>
</head>
<body>
<div class="sheet">
  <div class="hero-photo" role="img" aria-label="Greyscale photo of a trainer coaching people in a workout gym"></div>
  <div class="hero-shade"></div>

  <div class="contact">
    <div class="contact-row">
      <span class="contact-icon"><svg width="14" height="11" viewBox="0 0 14 11"><rect x="0.5" y="0.5" width="13" height="10" fill="none" stroke="#fff"/><path d="M0.5 0.5 L7 6 L13.5 0.5" fill="none" stroke="#fff"/></svg></span>
      <span>hello@clearpath-mktg.com</span>
    </div>
    <div class="contact-row">
      <span class="contact-icon"><svg width="14" height="14" viewBox="0 0 14 14"><path d="M3 1 L5.5 4 L4 5.5 C5 8 6 9 8.5 10 L10 8.5 L13 11 L11 13 C6 13 1 8 1 3 Z" fill="#fff"/></svg></span>
      <span>+65 6000 4821</span>
    </div>
  </div>

  <div class="brand">
    <span class="brand-mark"></span>
    <div class="brand-text">
      <span class="brand-name">Clearpath Marketing</span>
      <span class="brand-tag">Training that hits targets</span>
    </div>
  </div>

  <div class="title">
    <div class="title-line">MARKETING SKILL</div>
    <div class="title-accent">“WORKOUTS”</div>
  </div>

  <div class="promo-band">
    <div class="promo-question">NO TIME TO LEARN?</div>
    <div class="promo-answer">Problem solved with 1 day intensive workshops that will drive business growth and motivate your team.</div>
  </div>

  <section class="topics">
    <h2 class="section-title">KEY TOPICS:</h2>
    <ul class="topic-list">
      <li>Developing Strong Brand Plans</li>
      <li>Writing inspiring Briefs/Creative Evaluation</li>
      <li>Shopper Marketing/Developing Retail Promotions</li>
      <li>Brilliant Launch Management</li>
      <li>Improving Marketing R.O.I.</li>
      <li>Driving Brand Growth without Product Innovation</li>
      <li>Insight/Concept Development</li>
      <li>Integrating Digital Channels</li>
      <li>Creativity and Idea Generation</li>
    </ul>
  </section>

  <div class="divider"></div>

  <section class="benefits">
    <h2 class="section-title">KEY BENEFITS:</h2>
    <ul class="benefit-list">
      <li class="benefit">
        <svg class="benefit-icon" viewBox="0 0 52 52"><rect x="4" y="30" width="9" height="18" fill="var(--red)"/><rect x="17" y="22" width="9" height="26" fill="var(--red)"/><rect x="30" y="14" width="9" height="34" fill="var(--red)"/><rect x="43" y="6" width="8" height="42" fill="var(--red)"/></svg>
        <span class="benefit-text">Latest in world-class thinking/tools/case studies</span>
      </li>
      <li class="benefit">
        <svg class="benefit-icon" viewBox="0 0 52 52"><rect x="2" y="2" width="48" height="48" rx="6" fill="var(--red)"/><g stroke="#fff" stroke-width="3"><line x1="14" y1="10" x2="14" y2="42"/><line x1="26" y1="10" x2="26" y2="42"/><line x1="38" y1="10" x2="38" y2="42"/></g><g fill="#fff"><rect x="9" y="16" width="10" height="6"/><rect x="21" y="30" width="10" height="6"/><rect x="33" y="20" width="10" height="6"/></g></svg>
        <span class="benefit-text">Ability to “customize” to address your specific business issues</span>
      </li>
      <li class="benefit">
        <svg class="benefit-icon" viewBox="0 0 52 52"><rect x="6" y="2" width="40" height="48" rx="4" fill="var(--red)"/><g stroke="#fff" stroke-width="2.5" fill="none"><path d="M12 14 l3 3 l5 -6"/><path d="M12 27 l3 3 l5 -6"/><path d="M12 40 l3 3 l5 -6"/><line x1="25" y1="14" x2="39" y2="14"/><line x1="25" y1="27" x2="39" y2="27"/><line x1="25" y1="40" x2="39" y2="40"/></g></svg>
        <span class="benefit-text">Take-away “checklists” to embed behaviors and skills</span>
      </li>
      <li class="benefit">
        <svg class="benefit-icon" viewBox="0 0 52 52"><circle cx="26" cy="26" r="23" fill="var(--red)"/><g stroke="#fff" stroke-width="2" fill="none"><ellipse cx="26" cy="26" rx="10" ry="23"/><line x1="3" y1="26" x2="49" y2="26"/><path d="M7 14 H45 M7 38 H45"/></g></svg>
        <span class="benefit-text">Asian context / relevance</span>
      </li>
      <li class="benefit">
        <svg class="benefit-icon" viewBox="0 0 52 52"><path d="M16 30 L10 50 L18 46 L22 52 L26 34 Z M36 30 L42 50 L34 46 L30 52 L26 34 Z" fill="var(--red-dark)"/><circle cx="26" cy="20" r="18" fill="var(--red)"/><circle cx="26" cy="20" r="10" fill="none" stroke="#fff" stroke-width="2.5"/></svg>
        <span class="benefit-text">Proven quality</span>
      </li>
    </ul>
  </section>

  <footer class="why-band">
    <div class="why-head"><em>WHY ME?</em> - World Class Quality without the costs</div>
    <p class="why-body">The latest thinking, made practical and actionable.<br>20 years of business experience combined with over 10 years of proven training/facilitation for major “blue-chip” clients, regularly scoring 90%+ satisfaction.</p>
  </footer>
</div>
</body>
</html>
```